Cobalto Regal

I want a glossy card on both sides. We sell underwater LED lights for water craft

we sell custom audio enclosures for automobile, boats and atv's.

view our websites for any other pictures you may think are better suited.

Industry/Entity Type

Audio

Contact Information for Business Card

Email address: CobaltoRegal@mailbarn.net
Website: www.hullglowcap.com
underwater LED lighting for watercraft
boat drain plug lights
phone number: 555-271-6048

other side of card:
email address the same
website: www.versatilesoundshells.com
speaker enclosures, auto, boat and atv
same phone number

```html
<!DOCTYPE html>
<html lang="en">
<head>
<meta charset="utf-8">
<title>Cobalto Regal — Business Card</title>
<link rel="stylesheet" href="https://fonts.googleapis.com/css2?family=Kaushan+Script&family=Open+Sans:wght@300;400;700&display=swap">
<style>
  :root {
    --page-bg: #e4e4e2;
    --card-dark: #0a0f15;
    --card-light: #ffffff;
    --ink-dark: #111111;
    --ink-mid: #333333;
    --ink-light: #ffffff;
    --ink-soft: #d8e2ea;
    --rule-dark: #8b98a4;
    --rule-light: #9a9a9a;
    --panel-grey-1: #f2f2f2;
    --panel-grey-2: #cfcfcf;
    --panel-grey-3: #8a8a8a;
  }
  * { box-sizing: border-box; margin: 0; padding: 0; }
  html, body {
    width: 1200px; height: 803px; overflow: hidden;
    background: var(--page-bg);
    font-family: "Open Sans", Arial, sans-serif;
  }
  .canvas { position: relative; width: 1200px; height: 803px; }

  .card {
    position: absolute; top: 247px;
    width: 540px; height: 309px;
    overflow: hidden;
    box-shadow: 0 6px 18px rgba(0,0,0,0.22);
  }
  .card-front { left: 40px; background: var(--card-dark); }
  .card-back { left: 620px; background: var(--card-light); }

  .card svg.panels { position: absolute; inset: 0; width: 100%; height: 100%; }

  .brand-name {
    position: absolute;
    font-family: "Kaushan Script", cursive;
    white-space: nowrap;
    line-height: 1;
  }

  /* Front */
  .card-front .brand-name {
    left: 120px; top: 62px;
    font-size: 54px; color: var(--ink-light);
  }
  .front-info { position: absolute; left: 268px; top: 140px; width: 250px; color: var(--ink-light); }
  .front-tagline {
    font-weight: 300; font-size: 12.5px; letter-spacing: 0.6px;
    text-transform: uppercase; line-height: 1.35; color: var(--ink-soft);
    padding-bottom: 9px; border-bottom: 1px solid var(--rule-dark);
  }
  .front-contact { margin-top: 10px; font-size: 13px; line-height: 1.45; }
  .front-contact .site { font-weight: 700; font-size: 13.5px; }
  .front-contact .email, .front-contact .phone { font-weight: 400; }

  /* Back */
  .back-info { position: absolute; left: 26px; top: 150px; width: 300px; color: var(--ink-dark); }
  .back-heading { display: flex; gap: 14px; align-items: baseline; }
  .back-heading .service { font-weight: 700; font-size: 12.5px; text-transform: uppercase; }
  .back-heading .markets { font-weight: 300; font-size: 14px; color: var(--ink-mid); }
  .back-heading .markets strong { font-weight: 700; color: var(--ink-dark); }
  .card-back .brand-name {
    position: static; display: block;
    margin-top: 10px; font-size: 40px; color: var(--ink-dark);
  }
  .back-contact { margin-top: 8px; font-size: 13px; line-height: 1.5; color: var(--ink-mid); }
  .back-contact .site { font-weight: 700; color: var(--ink-dark); }
</style>
</head>
<body>
<main class="canvas">

  <section class="card card-front" aria-label="Business card, front">
    <svg class="panels" viewBox="0 0 540 309" preserveAspectRatio="none" role="img" aria-label="Collage of boats lit at night by underwater LED lights">
      <defs>
        <linearGradient id="glow-green" x1="0" y1="0" x2="1" y2="1">
          <stop offset="0" stop-color="#2aa0b0"/>
          <stop offset="0.5" stop-color="#3fbf6a"/>
          <stop offset="1" stop-color="#0d2a5a"/>
        </linearGradient>
        <linearGradient id="sunset" x1="0" y1="1" x2="1" y2="0">
          <stop offset="0" stop-color="#d9823a"/>
          <stop offset="0.5" stop-color="#3b4f8a"/>
          <stop offset="1" stop-color="#1a2c5c"/>
        </linearGradient>
        <linearGradient id="deep-blue" x1="0" y1="0" x2="1" y2="1">
          <stop offset="0" stop-color="#1f3e78"/>
          <stop offset="1" stop-color="#0b1730"/>
        </linearGradient>
        <linearGradient id="teal-night" x1="0" y1="0" x2="0" y2="1">
          <stop offset="0" stop-color="#173a44"/>
          <stop offset="1" stop-color="#0a161c"/>
        </linearGradient>
        <radialGradient id="beam" cx="0.45" cy="0.45" r="0.7">
          <stop offset="0" stop-color="#3a4652"/>
          <stop offset="1" stop-color="#070b10"/>
        </radialGradient>
      </defs>
      <rect width="540" height="309" fill="url(#beam)"/>
      <polygon points="0,0 170,0 110,150 0,200" fill="url(#deep-blue)"/>
      <polygon points="0,200 110,150 200,309 0,309" fill="url(#sunset)"/>
      <polygon points="110,150 170,0 250,0 230,170" fill="url(#glow-green)"/>
      <polygon points="110,150 230,170 260,309 200,309" fill="url(#teal-night)"/>
      <g stroke="#0a0f15" stroke-width="2" fill="none">
        <polyline points="170,0 110,150 0,200"/>
        <polyline points="110,150 200,309"/>
        <polyline points="110,150 230,170 260,309"/>
        <polyline points="230,170 250,0"/>
      </g>
    </svg>
    <h1 class="brand-name">Cobalto Regal</h1>
    <div class="front-info">
      <p class="front-tagline">Underwater LED lighting or<br>watercraft boat drain plug<br>lights</p>
      <p class="front-contact">
        <span class="site">www.hullglowcap.com</span><br>
        <span class="email">CobaltoRegal@mailbarn.net</span><br>
        <span class="phone">555-271-6048</span>
      </p>
    </div>
  </section>

  <section class="card card-back" aria-label="Business card, back">
    <svg class="panels" viewBox="0 0 540 309" preserveAspectRatio="none">
      <defs>
        <radialGradient id="speaker-large" cx="0.6" cy="0.45" r="0.55">
          <stop offset="0" stop-color="var(--panel-grey-3)"/>
          <stop offset="0.6" stop-color="var(--panel-grey-2)"/>
          <stop offset="1" stop-color="var(--panel-grey-1)"/>
        </radialGradient>
        <radialGradient id="speaker-small" cx="0.5" cy="0.5" r="0.5">
          <stop offset="0" stop-color="var(--panel-grey-3)"/>
          <stop offset="1" stop-color="var(--panel-grey-1)"/>
        </radialGradient>
      </defs>
      <polygon points="330,0 540,0 540,130 380,120" fill="url(#speaker-large)" role="img" aria-label="Black speaker pod enclosure with chrome grille"/>
      <polygon points="20,0 330,0 300,130 20,90" fill="url(#speaker-small)" opacity="0.55" role="img" aria-label="Round chrome marine speaker"/>
      <polygon points="380,120 540,130 540,309 470,309" fill="url(#speaker-small)" opacity="0.6" role="img" aria-label="Small tweeter pod"/>
      <g stroke="var(--rule-light)" stroke-width="1.2" fill="none">
        <polyline points="0,90 20,90 300,130 330,0"/>
        <polyline points="300,130 380,120 540,130"/>
        <polyline points="380,120 470,309"/>
      </g>
    </svg>
    <div class="back-info">
      <div class="back-heading">
        <span class="service">Speaker Enclosures</span>
        <span class="markets">Auto, Boat and <strong>ATV</strong></span>
      </div>
      <h2 class="brand-name">Cobalto Regal</h2>
      <p class="back-contact">
        555-271-6048<br>
        CobaltoRegal@mailbarn.net<br>
        <span class="site">www.versatilesoundshells.com</span>
      </p>
    </div>
  </section>

</main>
</body>
</html>
```